Unique Business Card Design

Unique Business Card design for our orthotic and prosthetic company. Our logo is on our website, color is light blue. Unique shape (artificial leg shaped, vertical, etc..) preferred. Logo, business name, individual name and basic demographics needed.

Industry/Entity Type

Business

Contact Information for Business Card

Logo, Industry, Phone # Logo, "Prosthetic & Orthotic Services" Place to add individual name and contact info

Colors
cee9f5

Requirements
Must have
• The icon must be there, placement of "Prosthetic & Orthotic Services" can be moved
Nice to have
• Like the mix of light blue, and a little darker blue. One design included the icons from my website which was a nice touch

```html
<!DOCTYPE html>
<html lang="en">
<head>
<meta charset="utf-8">
<title>Stridewell Inc. Business Card</title>
<link href="https://fonts.googleapis.com/css2?family=Source+Sans+3:ital,wght@0,400;0,600;0,700;1,400&family=Crimson+Text:ital@1&display=swap" rel="stylesheet">
<style>
  :root {
    --page-bg: #ecebe8;
    --card-white: #ffffff;
    --brand-blue: #1a5ea8;
    --brand-light: #cee9f5;
    --pattern-tint: #eef6fb;
    --text-dark: #2b2b2b;
    --text-muted: #4a4a4a;
    --divider-soft: #d5e7f1;
  }
  * { margin: 0; padding: 0; box-sizing: border-box; }
  html, body {
    width: 1100px; height: 1200px; overflow: hidden;
    background: var(--page-bg);
    font-family: "Source Sans 3", "Myriad Pro", Arial, sans-serif;
  }
  .business-card {
    position: absolute; left: 167px; top: 335px;
    width: 760px; height: 435px;
    background: var(--card-white);
    overflow: hidden;
  }
  .icon-pattern {
    position: absolute; left: 0; top: 0; width: 760px; height: 352px;
    background: linear-gradient(180deg, var(--pattern-tint) 0%, #ffffff 45%, #ffffff 60%, var(--pattern-tint) 100%);
  }
  .brand-mark {
    position: absolute; left: 29px; top: 131px;
    width: 80px; height: 80px; border-radius: 50%;
    background: var(--brand-blue);
  }
  .brand-name {
    position: absolute; left: 129px; top: 141px;
    font-size: 25px; font-weight: 600; color: var(--brand-blue);
    letter-spacing: -0.3px; line-height: 1;
  }
  .brand-rule {
    position: absolute; left: 131px; top: 173px;
    width: 200px; height: 2px; background: var(--brand-blue);
  }
  .brand-tagline {
    position: absolute; left: 142px; top: 176px;
    font-family: "Crimson Text", Georgia, serif; font-style: italic;
    font-size: 15px; color: var(--brand-blue); line-height: 1.2;
  }
  .divider { position: absolute; left: 400px; width: 3px; }
  .divider--name { top: 85px; height: 45px; background: var(--brand-blue); }
  .divider--contact { top: 168px; height: 90px; background: var(--divider-soft); }
  .person-name {
    position: absolute; left: 434px; top: 80px;
    font-size: 27px; color: var(--brand-blue); line-height: 1;
  }
  .person-name strong { font-weight: 700; }
  .person-title {
    position: absolute; left: 433px; top: 109px;
    font-size: 18px; font-style: italic; color: var(--text-muted); line-height: 1;
  }
  .contact-list { position: absolute; left: 434px; top: 166px; list-style: none; }
  .contact-item {
    display: flex; align-items: center; height: 26px; margin-bottom: 6.5px;
    font-size: 15.5px; color: var(--text-dark);
  }
  .contact-icon {
    width: 26px; height: 26px; border-radius: 50%;
    background: var(--brand-blue); margin-right: 12px; flex: none;
    display: flex; align-items: center; justify-content: center;
  }
  .footer-address {
    position: absolute; left: 0; top: 352px; width: 401px; height: 83px;
    background: var(--brand-light);
    display: flex; align-items: center; padding-left: 52px;
    font-size: 16px; color: var(--text-dark);
  }
  .footer-cell {
    position: absolute; left: 401px; top: 352px; width: 359px; height: 83px;
    background: var(--brand-blue);
    display: flex; align-items: center; justify-content: center;
    font-size: 18px; font-weight: 700; letter-spacing: 4.6px; color: #ffffff;
  }
</style>
</head>
<body>
  <div class="business-card">
    <div class="icon-pattern" role="img" aria-label="Faint pattern of prosthetic limb, crutch and mobility icons"></div>

    <div class="brand-mark"></div>
    <div class="brand-name">STRIDEWELL INC.</div>
    <div class="brand-rule"></div>
    <div class="brand-tagline">Prosthetic &amp; Orthotic Services</div>

    <div class="divider divider--name"></div>
    <div class="person-name"><strong>Mira</strong> Halvorsen</div>
    <div class="person-title">Orthotist/Prosthetist</div>

    <div class="divider divider--contact"></div>
    <ul class="contact-list">
      <li class="contact-item">
        <span class="contact-icon">
          <svg width="14" height="14" viewBox="0 0 24 24"><path fill="#fff" d="M6.6 10.8a15.1 15.1 0 0 0 6.6 6.6l2.2-2.2a1 1 0 0 1 1-.25 11.4 11.4 0 0 0 3.6.57 1 1 0 0 1 1 1V20a1 1 0 0 1-1 1A17 17 0 0 1 3 4a1 1 0 0 1 1-1h3.5a1 1 0 0 1 1 1c0 1.25.2 2.45.57 3.57a1 1 0 0 1-.25 1z"/></svg>
        </span>
        555 . 014 . 2760 / Fax 555 . 014 . 2781
      </li>
      <li class="contact-item">
        <span class="contact-icon">
          <svg width="14" height="14" viewBox="0 0 24 24"><rect x="2" y="5" width="20" height="14" fill="none" stroke="#fff" stroke-width="2"/><path d="M2 5l10 8 10-8" fill="none" stroke="#fff" stroke-width="2"/></svg>
        </span>
        Mhalvorsen@stridewellinc.com
      </li>
      <li class="contact-item">
        <span class="contact-icon">
          <svg width="14" height="14" viewBox="0 0 24 24"><rect x="3" y="4" width="18" height="12" fill="none" stroke="#fff" stroke-width="2.4"/><path d="M8 20h8M12 16v4" stroke="#fff" stroke-width="2.4"/></svg>
        </span>
        stridewellinc.com
      </li>
    </ul>

    <div class="footer-address">2250 Linden Ave. Brookfield, NY 10990</div>
    <div class="footer-cell">CELL: 555-0147392</div>
  </div>
</body>
</html>
```